Copper Gavel Auctions business card design with existing logo

Looking for a sleek and sexy design using our current logo

Contact Information for Business Card

Name, address, email, phone, website. Marcus Delvane 418 Birchmont Road Suite 200C Fenwick NY 11093 Copperbidhouse.net (631)582-4067

```html
<!DOCTYPE html>
<html lang="en">
<head>
<meta charset="utf-8">
<title>Copper Gavel Auctions – Business Card</title>
<link href="https://fonts.googleapis.com/css2?family=Lato:wght@400;700;900&display=swap" rel="stylesheet">
<style>
  :root {
    --backdrop: #1c1c1d;
    --brand-red: #d42027;
    --brand-navy: #1f3a8a;
    --card-white: #ffffff;
    --text-navy: #22357f;
  }
  * { margin: 0; padding: 0; box-sizing: border-box; }
  html, body {
    width: 1200px; height: 1200px; overflow: hidden;
    background: var(--backdrop);
    font-family: "Lato", sans-serif;
  }
  .stage { position: relative; width: 1200px; height: 1200px; }

  .card {
    position: absolute;
    left: 220px;
    width: 760px;
    height: 434px;
    border-radius: 22px;
    overflow: hidden;
  }

  /* Front card */
  .card-front {
    top: 110px;
    background: var(--brand-red);
    display: flex; flex-direction: column; align-items: center; justify-content: center;
    gap: 26px;
  }
  .front-mark {
    width: 96px; height: 96px; border-radius: 50%;
    background: var(--card-white);
  }
  .front-name {
    color: var(--card-white);
    font-weight: 900;
    font-size: 52px;
    letter-spacing: 4px;
    text-transform: uppercase;
    text-align: center;
    line-height: 1.1;
  }

  /* Back card */
  .card-back {
    top: 600px;
    background: var(--card-white);
    border-bottom: 8px solid var(--brand-red);
  }
  .back-brand {
    position: absolute; left: 54px; top: 48px;
    display: flex; align-items: center; gap: 18px;
  }
  .back-mark {
    width: 62px; height: 62px; border-radius: 50%;
    background: var(--brand-red);
  }
  .back-name {
    color: var(--text-navy);
    font-weight: 900;
    font-size: 30px;
    letter-spacing: 2px;
    text-transform: uppercase;
    line-height: 1.1;
  }
  .person-name {
    position: absolute; right: 44px; top: 150px;
    color: var(--text-navy);
    font-weight: 900;
    font-size: 24px;
    letter-spacing: 1px;
    text-transform: uppercase;
  }
  .name-tab {
    position: absolute; right: 0; top: 140px;
    width: 18px; height: 48px;
    background: var(--brand-red);
  }
  .contact-list {
    position: absolute; left: 54px; bottom: 54px;
    list-style: none;
    color: var(--text-navy);
    font-size: 21px;
    line-height: 1.5;
  }
  .contact-list li { display: flex; align-items: center; gap: 12px; }
  .contact-list svg { width: 16px; height: 16px; flex: none; fill: var(--brand-red); }
  .address {
    position: absolute; right: 44px; bottom: 46px;
    text-align: right;
    color: var(--text-navy);
    font-size: 22px;
    line-height: 1.4;
    font-style: normal;
  }
</style>
</head>
<body>
<main class="stage">
  <section class="card card-front">
    <span class="front-mark" aria-hidden="true"></span>
    <h1 class="front-name">Copper Gavel<br>Auctions</h1>
  </section>

  <section class="card card-back">
    <div class="back-brand">
      <span class="back-mark" aria-hidden="true"></span>
      <h2 class="back-name">Copper Gavel<br>Auctions</h2>
    </div>

    <p class="person-name">Marcus Delvane</p>
    <span class="name-tab" aria-hidden="true"></span>

    <ul class="contact-list">
      <li>
        <svg viewBox="0 0 24 24" aria-hidden="true"><path d="M6.6 10.8a15.1 15.1 0 0 0 6.6 6.6l2.2-2.2a1 1 0 0 1 1-.25 11.4 11.4 0 0 0 3.6.57 1 1 0 0 1 1 1V20a1 1 0 0 1-1 1A17 17 0 0 1 3 4a1 1 0 0 1 1-1h3.5a1 1 0 0 1 1 1c0 1.25.2 2.45.57 3.57a1 1 0 0 1-.25 1z"/></svg>
        (631)582-4067
      </li>
      <li>
        <svg viewBox="0 0 24 24" aria-hidden="true"><path d="M2 5h20v14H2z M2 5l10 8 10-8" stroke="#fff" stroke-width="1.6"/></svg>
        info@copperbidhouse.com
      </li>
      <li>
        <svg viewBox="0 0 24 24" aria-hidden="true"><circle cx="12" cy="12" r="10"/><path d="M2 12h20M12 2c3 3 3 17 0 20M12 2c-3 3-3 17 0 20" stroke="#fff" stroke-width="1.4" fill="none"/></svg>
        www.Copperbidhouse.net
      </li>
    </ul>

    <address class="address">
      418 Birchmont Road<br>
      Suite 200C<br>
      Fenwick NY 11093
    </address>
  </section>
</main>
</body>
</html>
```